Dance School Banner Design

Design a banner with landscape orientation for outdoor use and advertisement for Dance School.

Tha dance school is Marlow Street Dance Studio and they have their own logo (please message for the file to be sent to you) utilising lots of colour.

Their brand and uniform colours are purple and golden yellow.

Must have the name/logo.

Must attract all ages, boys and girls.

MSDS offers dance class for all ages and all levels of ability in the following dance styles:

Classical Ballet
Jazz
Tap
Modern / Contemporary
Hip Hop
Cheerleading
Vimbo (licensed logo is available please message for this)
Vimbokinetic (licensed logo is available please message for this)
Boys Class
Adults Classes

They offer all classes for fun or for competition.

Offer exams in Classical Ballet, Jazz and Tap.

Target Market(s)

All ages

Industry/Entity Type

Landscape

Requirements
Must have
• What classes are offered

Logo - 2 designs uploaded must use Marlow Street Dance Studio one, may wish to include home of "KESTRELS" logo aswell please message for this to be sent to you

Phone Number 0455 316 904

Email address marlow-steps@mailbreeze.net

website address marlowstreetsteps.com (this website is not live yet please see preview by using this link http://preview.dev.qelbrix.com/index.php?admin_action=preview_mod&site_id=5820471396&template_id=739&industry=qelbrixsites.com)
Nice to have
• Images of dancers (can provide some if needed)
Should not have
• Anything vulgar or discriminatory

```html
<!DOCTYPE html>
<html lang="en">
<head>
<meta charset="utf-8">
<title>Marlow Street Dance Studio – Dance Class Banner</title>
<link rel="stylesheet" href="https://fonts.googleapis.com/css2?family=Arimo:wght@400;700&family=Mali:wght@400&display=swap">
<style>
:root{
  --purple:#6a2a8e;
  --purple-deep:#5a1f7c;
  --gold:#c9a03a;
  --white:#ffffff;
  --ink:#1c1c1c;
}
html,body{margin:0;padding:0;overflow:hidden;background:#fff}
.banner{position:relative;width:1200px;height:477px;overflow:hidden;background:var(--white);font-family:Arimo,Arial,sans-serif}
.backdrop{position:absolute;inset:0}
.exams{position:absolute;left:48px;top:26px;width:170px;color:var(--white);font-weight:700;text-align:center;line-height:1.12}
.exams .lead{font-size:25px;display:block;margin-bottom:4px}
.exams .styles{font-size:20px}
.tagline{position:absolute;left:335px;top:36px;width:840px;color:var(--white);font-weight:700;font-size:30px;letter-spacing:.3px;white-space:nowrap}
.class-box{position:absolute;left:313px;top:132px;width:428px;height:64px;background:var(--purple);border-radius:18px 18px 0 18px;color:var(--white);text-align:center}
.class-box h1{margin:0;font-family:Mali,cursive;font-weight:400;font-size:52px;line-height:52px;margin-top:-12px}
.class-box p{margin:0;font-size:20px;line-height:22px}
.styles-list{position:absolute;top:206px;margin:0;padding:0;list-style:none;font-weight:700;font-size:16px;color:var(--ink)}
.styles-list li{position:relative;padding-left:22px;height:21.5px;line-height:21.5px}
.styles-list li::before{content:"";position:absolute;left:0;top:6px;width:6px;height:6px;border:2.5px solid var(--purple);border-radius:50%}
.col-a{left:337px}
.col-b{left:517px}
.contact{position:absolute;left:452px;top:332px;width:289px;height:89px;background:var(--gold);border-radius:14px 14px 0 0;color:var(--white);text-align:center}
.contact .phone{display:block;font-weight:700;font-size:29px;margin-top:6px}
.contact .line{display:block;font-size:17px;line-height:21px}
.brand{position:absolute;left:44px;top:350px;display:flex;align-items:center;gap:12px;color:var(--purple);font-weight:700;font-size:30px;line-height:1}
.brand .dot{width:26px;height:26px;border-radius:50%;background:var(--gold)}
.photo{position:absolute}
.photo-kids{left:196px;top:198px;width:116px;height:134px;border-radius:40px;background:radial-gradient(circle at 50% 45%,#e9c79f,#c98bb5 55%,rgba(255,255,255,0) 72%)}
.photo-boy{left:718px;top:92px;width:210px;height:330px;border-radius:90px;background:radial-gradient(ellipse at 50% 45%,#2f9fd6 0%,#233046 50%,rgba(255,255,255,0) 72%)}
.photo-woman{left:900px;top:6px;width:270px;height:430px;border-radius:120px;background:radial-gradient(ellipse at 50% 45%,#f2d7c2 0%,#2a2630 45%,rgba(255,255,255,0) 70%)}
</style>
</head>
<body>
<div class="banner">
  <svg class="backdrop" width="1200" height="477" viewBox="0 0 1200 477" aria-hidden="true">
    <path d="M0 0H1200V32H300Q296 150 215 200Q130 238 0 240Z" fill="var(--purple)"/>
    <path d="M0 252Q150 248 232 205Q305 160 308 40" fill="none" stroke="var(--gold)" stroke-width="8"/>
    <rect x="290" y="32" width="910" height="60" fill="var(--gold)"/>
    <path d="M0 477V436H690Q950 432 1050 330Q1120 255 1200 222V477Z" fill="var(--purple)"/>
    <path d="M0 428H690Q945 424 1045 318Q1118 240 1200 205" fill="none" stroke="var(--gold)" stroke-width="9"/>
  </svg>

  <div class="exams"><span class="lead">Exams in</span><span class="styles">Classical Ballet<br>Jazz and Tap</span></div>
  <div class="tagline">All Classes For FUN or For COMPETITION</div>

  <div class="class-box">
    <h1>Dance Class</h1>
    <p>for all ages and all levels of ability</p>
  </div>

  <ul class="styles-list col-a">
    <li>Jazz</li><li>Tap</li><li>Hip Hop</li><li>Boys Class</li><li>Adults Classes</li>
  </ul>
  <ul class="styles-list col-b">
    <li>Vimbo</li><li>Vimbokinetic</li><li>Cheerleading</li><li>Classical Ballet</li><li>Modern / Contemporary</li>
  </ul>

  <div class="contact">
    <span class="phone">Call: 0455 316 904</span>
    <span class="line">marlow-steps@mailbreeze.net</span>
    <span class="line">www.marlowstreetsteps.com</span>
  </div>

  <div class="brand"><span class="dot"></span><span>Marlow Street<br>Dance Studio</span></div>

  <div class="photo photo-kids" role="img" aria-label="Two young girls jumping mid-air in dance clothes"></div>
  <div class="photo photo-boy" role="img" aria-label="Boy in blue shirt doing a hip hop dance move"></div>
  <div class="photo photo-woman" role="img" aria-label="Young woman leaping in a jazz dance pose"></div>
</div>
</body>
</html>
```